Business Card Design

Online clothing womens clothing store, I sell my clothing online and at the markets.

i would like the attached picture on the front of the card and the contact information on the back.

Industry/Entity Type

Business

Contact Information for Business Card

Velvet Harbour
Marnie Talbot
(Instagram symbol) _velvet_harbour_
(Facebook symbol) www.facepage-example.com/velvetharbourau/

W : www.velvetharbour-example.com.au
E : info@velvetharbour-example.com.au
P : 0491876324

```html
<!DOCTYPE html>
<html lang="en">
<head>
<meta charset="utf-8">
<title>Velvet Harbour — Business Card</title>
<link href="https://fonts.googleapis.com/css2?family=Barlow:wght@400&family=Cabin:wght@400;600&display=swap" rel="stylesheet">
<style>
  :root {
    --page: #ece6dc;
    --card: #ffffff;
    --ink: #111111;
    --shadow: rgba(0,0,0,0.28);
    --sea-1: #c9c2b8;
    --sea-2: #3c3430;
    --sea-3: #a8323f;
    --sea-4: #c7ab92;
    --sea-5: #ece9e4;
    --sky: #dce6ea;
    --smoke-light: #d6e0df;
    --smoke-dark: #3b4550;
  }
  * { margin: 0; padding: 0; box-sizing: border-box; }
  html, body { width: 1189px; height: 1200px; overflow: hidden; }
  body {
    background: var(--page);
    font-family: "Cabin", sans-serif;
    color: var(--ink);
    position: relative;
  }
  .card {
    position: absolute;
    left: 145px;
    width: 900px;
    height: 554px;
    background: var(--card);
    box-shadow: 6px 8px 10px var(--shadow);
    overflow: hidden;
  }
  .card--front { top: 26px; }
  .card--back { top: 620px; }

  .lookbook {
    display: flex;
    height: 415px;
  }
  .lookbook__panel {
    flex: 1;
    background: linear-gradient(180deg, var(--sky) 0%, var(--sky) 40%, var(--tone) 55%, var(--tone) 85%, #e8dccb 100%);
  }
  .lookbook__panel:nth-child(1) { --tone: var(--sea-1); }
  .lookbook__panel:nth-child(2) { --tone: var(--sea-2); }
  .lookbook__panel:nth-child(3) { --tone: var(--sea-3); }
  .lookbook__panel:nth-child(4) { --tone: var(--sea-4); }
  .lookbook__panel:nth-child(5) { --tone: var(--sea-5); }

  .wordmark {
    position: absolute;
    left: 0; right: 0;
    text-align: center;
    font-family: "Barlow", sans-serif;
    font-weight: 400;
    font-size: 56px;
    letter-spacing: 0.22em;
    padding-left: 0.22em;
    color: var(--ink);
    line-height: 1;
  }
  .card--front .wordmark { top: 455px; }
  .card--back .wordmark { top: 443px; }

  .mood {
    position: absolute;
    left: 0; top: 34px;
    width: 470px; height: 316px;
    background: radial-gradient(ellipse at 80% 55%, var(--smoke-dark) 0%, #6b7680 35%, var(--smoke-light) 70%, #e4ebea 100%);
  }

  .contact {
    position: absolute;
    left: 502px; top: 78px;
    width: 380px;
  }
  .contact__name { font-size: 32px; font-weight: 600; line-height: 1; }
  .contact__role { font-size: 21px; font-weight: 400; margin-top: 2px; }
  .contact__list {
    list-style: none;
    margin-top: 78px;
    font-size: 21px;
    line-height: 30px;
  }
  .contact__list li { display: flex; align-items: center; gap: 8px; }
  .contact__icon { width: 22px; height: 22px; flex: none; }
</style>
</head>
<body>
  <section class="card card--front">
    <div class="lookbook">
      <div class="lookbook__panel" role="img" aria-label="Model on the beach in a patterned kimono"></div>
      <div class="lookbook__panel" role="img" aria-label="Model on the beach in a black maxi dress"></div>
      <div class="lookbook__panel" role="img" aria-label="Model on the beach in a red playsuit and hat"></div>
      <div class="lookbook__panel" role="img" aria-label="Model on the beach in a beige shirt dress"></div>
      <div class="lookbook__panel" role="img" aria-label="Model on the beach in a white fringed dress"></div>
    </div>
    <div class="wordmark">VELVET HARBOUR</div>
  </section>

  <section class="card card--back">
    <div class="mood" role="img" aria-label="Misty blue-grey brand mood image"></div>
    <div class="contact">
      <div class="contact__name">Marnie Talbot</div>
      <div class="contact__role">Managing Director</div>
      <ul class="contact__list">
        <li>
          <svg class="contact__icon" viewBox="0 0 22 22" aria-hidden="true">
            <rect x="1" y="1" width="20" height="20" rx="3" fill="#111"/>
            <path d="M5 9 Q11 4 17 9 L15 11 Q11 8 7 11 Z" fill="#fff"/>
            <rect x="7" y="11" width="8" height="6" fill="#fff"/>
          </svg>
          0491876324
        </li>
        <li>
          <svg class="contact__icon" viewBox="0 0 22 22" aria-hidden="true">
            <rect x="2" y="4" width="18" height="14" fill="none" stroke="#111" stroke-width="1.6"/>
            <path d="M2 4 L11 12 L20 4 M2 18 L9 10 M20 18 L13 10" fill="none" stroke="#111" stroke-width="1.4"/>
          </svg>
          info@velvetharbour-example.com.au
        </li>
        <li>
          <svg class="contact__icon" viewBox="0 0 22 22" aria-hidden="true">
            <rect x="2" y="2" width="18" height="18" rx="2" fill="#111"/>
          </svg>
          _velvet_harbour_
        </li>
        <li>
          <svg class="contact__icon" viewBox="0 0 22 22" aria-hidden="true">
            <rect x="2" y="2" width="18" height="18" rx="2" fill="#111"/>
          </svg>
          velvetharbourau
        </li>
      </ul>
    </div>
    <div class="wordmark">VELVET HARBOUR</div>
  </section>
</body>
</html>
```